Brightmend Outdoor Signage

We need an outdoor signage design for my company with new logo designed from artflockhub. We do electrical, Air conditioning & Plumbing, installation, service, repairs and maintenance. The design shall be an eye catching that cannot miss ready it.

Industry/Entity Type

Electrical, Air conditioning, Plumbing

```html
<!DOCTYPE html>
<html lang="en">
<head>
<meta charset="utf-8">
<title>Brightmend Outdoor Signage</title>
<link href="https://fonts.googleapis.com/css2?family=Anton&family=Montserrat:wght@700;800&display=swap" rel="stylesheet">
<style>
  :root {
    --blue: #1565b0;
    --blue-soft: #5a78b8;
    --red: #e3222a;
    --orange: #f08a3a;
    --yellow: #f2d21c;
    --green: #47b549;
    --green-soft: #6cc267;
    --brown: #8a5a3c;
    --sheet: #f1f1f1;
    --stage: #4a4a4a;
    --white: #ffffff;
  }
  * { box-sizing: border-box; margin: 0; padding: 0; }
  html, body { width: 1200px; height: 720px; overflow: hidden; }
  body { background: var(--stage); position: relative; font-family: 'Montserrat', sans-serif; }

  .signage {
    position: absolute; left: 20px; top: 65px;
    width: 1576px; height: 800px;
    transform: scale(0.736); transform-origin: 0 0;
    background: linear-gradient(120deg, #fafafa 0%, var(--sheet) 40%, #f7f7f7 60%, var(--sheet) 100%);
    overflow: hidden;
  }
  .signage__baseline { position: absolute; left: 0; bottom: 0; width: 100%; height: 8px; background: var(--blue); }

  /* brand block */
  .brand__mark { position: absolute; left: 300px; top: 80px; width: 170px; height: 170px; border-radius: 50%; background: var(--orange); }
  .brand__name { position: absolute; left: 70px; top: 300px; width: 560px; text-align: center; font-weight: 800; font-size: 92px; letter-spacing: -2px; color: var(--blue); line-height: 1; }
  .brand__trades { position: absolute; left: 72px; top: 440px; font-weight: 700; font-size: 29px; white-space: nowrap; }
  .brand__trades span { margin-right: 18px; }
  .trade--electrical { color: var(--red); }
  .trade--air { color: var(--blue); }
  .trade--plumbing { color: var(--orange); }

  /* emergency block */
  .emergency__swoosh { position: absolute; left: 170px; top: 490px; width: 240px; height: 190px; }
  .emergency__hours { position: absolute; left: 82px; top: 500px; font-family: 'Anton', sans-serif; font-size: 170px; line-height: 1; color: var(--blue); transform: skewX(-10deg); letter-spacing: -8px; }
  .emergency__label { position: absolute; left: 392px; top: 546px; font-family: 'Anton', sans-serif; font-size: 64px; line-height: 1; color: var(--blue); }
  .emergency__services { position: absolute; left: 394px; top: 617px; padding: 4px 10px; background: var(--red); font-family: 'Anton', sans-serif; font-size: 40px; line-height: 1.05; color: var(--white); letter-spacing: 1px; }

  .hotline { position: absolute; left: 70px; top: 686px; width: 612px; height: 76px; border-radius: 0 18px 18px 0; background: linear-gradient(90deg, var(--yellow) 8%, var(--orange) 50%, var(--red) 100%); }
  .hotline__icon { position: absolute; left: -4px; top: -3px; width: 82px; height: 82px; border-radius: 50%; background: var(--blue); border: 5px solid var(--white); display: flex; align-items: center; justify-content: center; }
  .hotline__number { position: absolute; left: 95px; top: 2px; font-weight: 800; font-size: 68px; line-height: 72px; color: var(--white); letter-spacing: 1px; }

  /* photo cluster */
  .photo { position: absolute; border-radius: 50%; border-style: solid; }
  .photo--electrical { left: 968px; top: 17px; width: 454px; height: 454px; border-width: 10px; border-color: var(--red); background: linear-gradient(135deg, #5a6068, #b9bcc2 50%, #2e3238); }
  .photo--aircon { left: 703px; top: 88px; width: 330px; height: 330px; border-width: 9px; border-color: var(--blue-soft); background: linear-gradient(135deg, #f3dca0, #c9c3b5 45%, #e06b28 85%); }
  .photo--plumbing { left: 988px; top: 240px; width: 252px; height: 252px; border-width: 8px; border-color: var(--orange); background: linear-gradient(135deg, #ecebe8, #d8b49e 55%, #cfd0d1); }
  .photo--cctv { left: 1238px; top: 200px; width: 282px; height: 282px; border-width: 9px; border-color: var(--green-soft); background: linear-gradient(160deg, #6f9fc8, #bcd3e6 55%, #5d8a5a); }
  .dot { position: absolute; border-radius: 50%; }
  .dot--orange { left: 703px; top: 113px; width: 76px; height: 76px; background: var(--orange); opacity: 0.75; }
  .dot--blue { left: 1378px; top: 100px; width: 76px; height: 76px; background: var(--blue-soft); opacity: 0.85; }

  /* service pills */
  .pill { position: absolute; height: 44px; border-radius: 0 14px 14px 0; color: var(--white); font-weight: 800; font-size: 31px; line-height: 44px; white-space: nowrap; }
  .pill__icon { position: absolute; left: -24px; top: -5px; width: 54px; height: 54px; border-radius: 50%; border: 3px solid var(--white); display: flex; align-items: center; justify-content: center; }
  .pill--electrical { left: 822px; top: 518px; width: 300px; padding-left: 42px; background: var(--blue); }
  .pill--plumbing { left: 1118px; top: 518px; width: 270px; padding-left: 42px; background: var(--red); }
  .pill--aircon { left: 730px; top: 590px; width: 420px; padding-left: 42px; background: var(--orange); }
  .pill--cctv { left: 1140px; top: 590px; width: 338px; padding-left: 46px; background: var(--green); }
  .icon--red { background: var(--red); }
  .icon--orange { background: var(--orange); }
  .icon--blue { background: var(--blue); }
  .icon--brown { background: var(--brown); }

  .scope { position: absolute; left: 738px; top: 664px; font-weight: 700; font-size: 28px; color: var(--blue); white-space: nowrap; }

  .web { position: absolute; left: 732px; top: 718px; width: 844px; height: 82px; }
  .web__text { position: absolute; left: 0; top: 20px; width: 100%; text-align: center; font-weight: 700; font-size: 32px; color: var(--white); }
  .web__name { color: var(--orange); }
</style>
</head>
<body>
  <main class="signage">
    <div class="brand__mark"></div>
    <h1 class="brand__name">Brightmend</h1>
    <p class="brand__trades"><span class="trade--electrical">Electrical</span><span class="trade--air">Air Conditioning</span><span class="trade--plumbing">Plumbing</span></p>

    <svg class="emergency__swoosh" viewBox="0 0 240 190" aria-hidden="true">
      <path d="M30 40 C90 -10 190 0 205 70 C215 120 180 160 150 185" fill="none" stroke="var(--orange)" stroke-width="22" stroke-linecap="round"/>
    </svg>
    <div class="emergency__hours">24/7</div>
    <div class="emergency__label">Emergency</div>
    <div class="emergency__services">SERVICES</div>

    <div class="hotline">
      <div class="hotline__icon">
        <svg width="40" height="40" viewBox="0 0 24 24" aria-hidden="true"><path d="M6.6 10.8a15 15 0 0 0 6.6 6.6l2.2-2.2c.3-.3.7-.4 1-.2 1.1.4 2.3.6 3.6.6.6 0 1 .4 1 1V20c0 .6-.4 1-1 1A17 17 0 0 1 3 4c0-.6.4-1 1-1h3.5c.6 0 1 .4 1 1 0 1.3.2 2.5.6 3.6.1.3 0 .7-.2 1z" fill="none" stroke="#fff" stroke-width="1.6"/></svg>
      </div>
      <div class="hotline__number">1300 555 019</div>
    </div>

    <div class="photo photo--electrical" role="img" aria-label="Gloved hands testing a switchboard with a multimeter"></div>
    <div class="photo photo--aircon" role="img" aria-label="Technician in hard hat servicing an outdoor air conditioning unit"></div>
    <div class="photo photo--plumbing" role="img" aria-label="Hands fitting a valve to a water pipe"></div>
    <div class="photo photo--cctv" role="img" aria-label="Dome security camera mounted outside a building"></div>
    <div class="dot dot--orange"></div>
    <div class="dot dot--blue"></div>

    <div class="pill pill--electrical"><span class="pill__icon icon--red"><svg width="26" height="26" viewBox="0 0 24 24" aria-hidden="true"><path d="M13 2 5 14h6l-1 8 8-12h-6z" fill="#fff"/></svg></span>ELECTRICAL</div>
    <div class="pill pill--plumbing"><span class="pill__icon icon--orange"><svg width="26" height="26" viewBox="0 0 24 24" aria-hidden="true"><path d="M12 3s-6 7-6 11a6 6 0 0 0 12 0c0-4-6-11-6-11z" fill="none" stroke="#fff" stroke-width="2"/></svg></span>PLUMBING</div>
    <div class="pill pill--aircon"><span class="pill__icon icon--blue"><svg width="26" height="26" viewBox="0 0 24 24" aria-hidden="true"><path d="M12 2v20M3.3 7l17.4 10M3.3 17 20.7 7" stroke="#fff" stroke-width="2"/></svg></span>AIR CONDITIONING</div>
    <div class="pill pill--cctv"><span class="pill__icon icon--brown"><svg width="26" height="26" viewBox="0 0 24 24" aria-hidden="true"><path d="M3 7l14 4-2 5L3 12zM15 14l3 4h3" fill="none" stroke="#fff" stroke-width="2" stroke-linejoin="round"/></svg></span>CCTV SECURITY</div>

    <p class="scope">Installation, Service, Repairs and Maintenance.</p>

    <div class="web">
      <svg width="844" height="82" viewBox="0 0 844 82" aria-hidden="true"><path d="M0 82 C20 82 24 70 30 50 L40 18 C45 5 52 0 70 0 L650 0 C668 0 676 5 682 16 L712 70 C717 78 724 82 740 82 Z" fill="var(--blue)"/></svg>
      <p class="web__text">www.<span class="web__name">Brightmend</span>Electrical.com.au</p>
    </div>

    <div class="signage__baseline"></div>
  </main>
</body>
</html>
```